Business card for communications

Need a business card for my consulting business - I work with not for profits, start ups and social enterprises on their media, communications campaigns.

Please see my website for colours, images and fonts www.morelbratton.example

Dana Morelbrat
Communications & Campaign strategist
Sydney - Melbourne
M: 0498 317 026
E: dana@morelbratton.example
S: danamorelbrat
W: morelbratton.example
T: @danamorelbrat

(above is info only and can be presented any way e.g. should not have to be M for mobile - it should be an icon)
Updates

Dear designers I have updated the brief and uploaded high res images from my website for you to use. The designs so far with the use of images and icons are much better so far. Thank you I look forward to receiving your revised designs. Dana Morelbrat

Industry/Entity Type

Communications

Font styles to use
Sans Serif

Requirements
Must have
• Icons for contact details
Images from the website www.morelbratton.example
Nice to have
• Images - attached

```html
<!DOCTYPE html>
<html lang="en">
<head>
<meta charset="utf-8">
<title>Dana Morelbrat – Business Card</title>
<link rel="stylesheet" href="https://fonts.googleapis.com/css2?family=Cousine&family=Source+Sans+3:ital,wght@0,400;0,600;0,700;1,400&display=swap">
<style>
  :root {
    --bg: #d9d9d9;
    --ink: #2b2b2b;
    --yellow-light: #fde23c;
    --yellow: #f8d21a;
    --yellow-deep: #f1c400;
    --fold: #d9b300;
    --wood-light: #e8c48f;
    --wood: #c98f4e;
    --wood-dark: #9a6a36;
    --paper: #f3f1ec;
    --avatar: #8a7f78;
    --avatar-ring: #2f2f2f;
  }
  * { box-sizing: border-box; margin: 0; padding: 0; }
  html, body {
    width: 1200px; height: 1000px; overflow: hidden;
    background: var(--bg);
  }
  .canvas {
    position: relative; width: 1200px; height: 1000px;
    display: flex; flex-direction: column; align-items: center; justify-content: center; gap: 60px;
  }
  .card {
    position: relative; width: 700px; height: 400px;
    border-radius: 26px; overflow: hidden;
    box-shadow: 0 8px 22px rgba(0,0,0,0.22);
  }

  /* Front */
  .card-front__image {
    position: absolute; inset: 0;
    background:
      radial-gradient(circle at 25% 30%, var(--paper) 0 8%, transparent 20%),
      radial-gradient(circle at 75% 70%, var(--paper) 0 7%, transparent 18%),
      radial-gradient(circle at 80% 20%, rgba(255,255,255,0.55) 0 6%, transparent 16%),
      linear-gradient(135deg, var(--wood-light), var(--wood) 55%, var(--wood-dark));
  }
  .card-front__name {
    position: absolute; inset: 0;
    display: flex; align-items: center; justify-content: center;
    font-family: "Cousine", monospace;
    font-size: 62px; letter-spacing: 6px; color: #1a1a1a;
    text-shadow: 0 0 10px rgba(255,255,255,0.8);
  }

  /* Back */
  .card-back {
    background: linear-gradient(160deg, var(--yellow-light), var(--yellow) 55%, var(--yellow-deep));
    color: var(--ink);
    font-family: "Source Sans 3", sans-serif;
  }
  .card-back__fold { position: absolute; inset: 0; }
  .identity {
    position: absolute; left: 36px; top: 32px;
    display: flex; align-items: center; gap: 20px;
  }
  .identity__portrait {
    width: 110px; height: 110px; border-radius: 50%;
    background: radial-gradient(circle at 50% 40%, #b4a79f, var(--avatar));
    border: 6px solid var(--avatar-ring);
  }
  .identity__name {
    font-family: "Cousine", monospace;
    font-size: 40px; letter-spacing: 3px; line-height: 1;
  }
  .identity__role { font-size: 17px; margin-top: 8px; }
  .contacts {
    position: absolute; left: 44px; top: 168px;
    list-style: none; font-size: 20px; line-height: 1;
  }
  .contacts li { display: flex; align-items: center; gap: 12px; margin-bottom: 10px; }
  .contacts__icon { width: 20px; height: 20px; flex: none; }
  .location { position: absolute; left: 44px; top: 322px; font-size: 19px; line-height: 1.25; }
  .location__cities { font-weight: 700; }
</style>
</head>
<body>
<main class="canvas">
  <section class="card card-front">
    <div class="card-front__image" role="img" aria-label="Blurred overhead photo of a shared work desk with laptops, notebooks and coffee"></div>
    <div class="card-front__name">DANA MORELBRAT</div>
  </section>

  <section class="card card-back">
    <svg class="card-back__fold" viewBox="0 0 700 400" aria-hidden="true">
      <path d="M300 400 C 420 300, 560 240, 700 200 L700 400 Z" fill="rgba(255,255,255,0.12)"/>
      <path d="M300 400 C 420 300, 560 240, 700 200" fill="none" stroke="var(--fold)" stroke-width="2"/>
    </svg>

    <div class="identity">
      <div class="identity__portrait" role="img" aria-label="Portrait photo of Dana Morelbrat"></div>
      <div>
        <div class="identity__name">DANA MORELBRAT</div>
        <div class="identity__role">Communications &amp; Campaign Strategist</div>
      </div>
    </div>

    <ul class="contacts">
      <li>
        <svg class="contacts__icon" viewBox="0 0 20 20" aria-hidden="true"><rect width="20" height="20" rx="4" fill="var(--ink)"/><path d="M6 4h3l1 3-2 1c1 2 2 3 4 4l1-2 3 1v3c-6 0-10-4-10-10z" fill="var(--yellow)"/></svg>
        0498 317 026
      </li>
      <li>
        <svg class="contacts__icon" viewBox="0 0 20 20" aria-hidden="true"><rect width="20" height="20" rx="4" fill="var(--ink)"/><rect x="4" y="6" width="12" height="8" fill="var(--yellow)"/><path d="M4 6l6 5 6-5" fill="none" stroke="var(--ink)" stroke-width="1.3"/></svg>
        dana@morelbratton.example
      </li>
      <li>
        <svg class="contacts__icon" viewBox="0 0 20 20" aria-hidden="true"><circle cx="10" cy="10" r="10" fill="var(--ink)"/></svg>
        www.morelbratton.example
      </li>
      <li>
        <svg class="contacts__icon" viewBox="0 0 20 20" aria-hidden="true"><circle cx="10" cy="10" r="10" fill="var(--ink)"/></svg>
        danamorelbrat
      </li>
      <li>
        <svg class="contacts__icon" viewBox="0 0 20 20" aria-hidden="true"><circle cx="10" cy="10" r="10" fill="var(--ink)"/></svg>
        @danamorelbrat
      </li>
    </ul>

    <div class="location">
      <div class="location__cities">Sydney - Melbourne</div>
      <div>Communications &amp; Campaign Strategist</div>
    </div>
  </section>
</main>
</body>
</html>
```